whitening gel shopping website design

Hello:
We would like to create a whitening gel selling website. It will be very close to Glowbrite, but different designs. https://us.glowbriteorals.example/

What is your organization or website name?
Velvet Beaming

Industry: health and beauty
Target user: ladies between 16 to 40, please make the website friendly and lovely

website pages: main website, shop products, enrolled monthly plans, about us, contact us, policy, customer login log out, shopping cart, customer dashboard.

Website main page contains:
1. one slide show that shows advertisements.
2. show current promo codes
3.show a brief overview about our history
4. show a brief overview about the product introduction
5. show a brief overview of our monthly enrolled product plan
6. have an area to show blogs and posts (please take a look at Glowbrite home page)
7. buttons for customer to login, sign up, visit home, about us, policy, returns, subscription etc.

Note: for the contest, please finish the website main page and the product page only, now we don’t have any logo, test or images, please use yours for now.

```html
<!DOCTYPE html>
<html lang="en">
<head>
<meta charset="utf-8">
<title>Velvet Beaming – Whitening Gel</title>
<link href="https://fonts.googleapis.com/css2?family=Poppins:wght@300;400;500;600;700&family=Great+Vibes&family=Playfair+Display:wght@700;900&display=swap" rel="stylesheet">
<style>
:root{
  --green:#3fa535;
  --green-light:#8fd16f;
  --green-pale:#c9efc0;
  --teal:#4fdcca;
  --teal-deep:#35cfbe;
  --mint:#a5f2df;
  --dark:#555555;
  --ink:#222222;
  --muted:#666666;
  --white:#ffffff;
  --blush:#ece3e3;
  --line:#dddddd;
}
*{margin:0;padding:0;box-sizing:border-box}
html,body{width:1200px;height:4063px;overflow:hidden;background:var(--white)}
body{position:relative;font-family:"Poppins",sans-serif;color:var(--ink)}
.abs{position:absolute}
.script{font-family:"Great Vibes",cursive;font-weight:400}
.serif{font-family:"Playfair Display",serif}
.ph{position:absolute}
.btn{position:absolute;display:flex;align-items:center;justify-content:center;gap:10px;border-radius:30px;background:var(--green);color:var(--white);font-weight:600;font-size:14px;letter-spacing:.5px;border:4px solid var(--green-pale)}

/* header */
.topbar{left:380px;top:0;width:433px;height:30px;background:var(--green);border-radius:0 0 8px 8px;display:flex;justify-content:space-around;align-items:center;color:var(--white);font-size:13px;font-weight:500}
.topbar span{display:flex;align-items:center;gap:6px}
.header{left:0;top:0;width:1200px;height:108px;background:var(--white);box-shadow:0 2px 6px rgba(0,0,0,.06)}
.logo{font-size:22px;font-weight:500;color:var(--ink);display:flex;align-items:center;gap:8px}
.logo i{width:14px;height:14px;background:var(--teal);display:inline-block}
.nav a{position:absolute;top:64px;font-size:14px;color:var(--muted);text-decoration:none}
.nav a.active{color:var(--green);font-weight:500}
.nav a.active::after{content:"";position:absolute;left:0;right:0;bottom:-38px;height:4px;background:var(--green)}

/* hero */
.hero-bg{left:0;top:108px;width:1200px;height:570px;background:linear-gradient(90deg,var(--teal-deep),var(--teal))}
.hero-1{left:149px;top:200px;font-size:66px;color:var(--white)}
.hero-2{left:220px;top:250px;font-size:130px;color:var(--white);line-height:1}
.hero-3{left:196px;top:350px;font-size:36px;letter-spacing:20px;color:var(--green);font-weight:600}
.hero-rule{left:149px;top:300px;width:60px;height:120px;border-left:2px solid var(--white);border-bottom:2px solid var(--white)}

/* history */
.watermark{left:122px;top:735px;width:948px;text-align:center;font-size:160px;font-weight:900;color:#eeeeee;letter-spacing:4px;font-family:"Playfair Display",serif}
.h-title{left:599px;top:915px;font-size:28px;color:var(--ink)}
.h-sub{left:599px;top:952px;font-size:26px;color:var(--ink);font-weight:700;font-family:"Playfair Display",serif}
.h-sub b{color:var(--green)}
.h-sub em{font-family:"Great Vibes",cursive;font-style:normal;font-weight:400;font-size:64px;line-height:.5}
.h-text{left:601px;top:1033px;width:440px;font-size:13px;line-height:20px;color:var(--muted)}

/* intro band */
.band{left:0;top:1238px;width:1200px;height:401px;background:var(--dark)}
.band-kicker{left:149px;top:1306px;font-size:14px;color:var(--white);font-weight:500}
.band-1{left:149px;top:1328px;font-size:58px;color:var(--green-light);font-weight:900;font-family:"Playfair Display",serif;letter-spacing:1px}
.band-2{left:149px;top:1386px;font-size:58px;color:var(--white);font-weight:900;font-family:"Playfair Display",serif;letter-spacing:1px}
.band-text{left:149px;top:1465px;font-size:14px;color:#e5e5e5}

/* product */
.frame{left:154px;top:1707px;width:252px;height:501px;border:12px solid var(--green-pale);border-right:none}
.frame-r1{left:378px;top:1707px;width:28px;height:12px;background:var(--green-pale)}
.thumb{width:56px;height:56px;border-radius:50%;background:var(--white);box-shadow:0 2px 10px rgba(0,0,0,.15)}
.p-title{left:588px;top:1728px;font-size:36px;font-weight:900;font-family:"Playfair Display",serif}
.p-sub{left:588px;top:1774px;font-size:14px;font-weight:600}
.stars{left:588px;top:1820px;width:98px;height:22px;background:var(--ink);display:flex;align-items:center;justify-content:center;gap:3px}
.reviews{left:704px;top:1823px;font-size:11px;color:var(--green)}
.p-text{left:588px;top:1896px;width:400px;font-size:11px;line-height:17px;color:var(--muted)}
.check{font-size:11px;color:var(--muted);display:flex;align-items:center;gap:8px}
.price{left:588px;top:2078px;font-size:28px;font-weight:700}
.qty{left:588px;top:2127px;width:157px;height:40px;border:1px solid var(--line);display:flex}
.qty span{flex:1;display:flex;align-items:center;justify-content:center;font-size:14px;color:var(--muted);border-right:1px solid var(--line)}
.qty span:last-child{border-right:none}

/* tabs */
.tabs-bg{left:0;top:2248px;width:1200px;height:605px;background:var(--mint)}
.tab-line{left:149px;top:2320px;width:902px;height:1px;background:#7fd9c3}
.tab{top:2278px;font-size:16px;font-weight:700;color:var(--green);transform:translateX(-50%)}
.tab.active::after{content:"";position:absolute;left:-8px;right:-8px;top:36px;height:4px;background:var(--green)}
.t-head{left:149px;font-size:19px;font-weight:700}
.t-text{left:149px;font-size:11px;line-height:20px;color:#444}

/* news */
.news-1{left:0;width:1200px;text-align:center;top:2880px;font-size:48px;font-weight:900;font-family:"Playfair Display",serif}
.news-2{left:600px;top:2932px;font-size:22px;font-weight:700;letter-spacing:4px;font-family:"Playfair Display",serif}
.date{width:64px;height:64px;background:var(--dark);border:4px solid var(--white);outline:2px solid var(--dark);color:var(--white);display:flex;flex-direction:column;align-items:center;justify-content:center;line-height:1}
.date b{font-size:18px}
.date small{font-size:10px}
.topic{font-size:10px;color:var(--muted);font-weight:500}
.n-title{font-size:16px;line-height:21px;width:220px}
.more{font-size:15px;color:var(--green)}

/* signup */
.sign-bg{left:0;top:3386px;width:1200px;height:266px;background:var(--blush)}
.s-title{left:163px;top:3435px;font-size:36px;font-weight:900;font-family:"Playfair Display",serif;color:#333}
.s-sub{left:163px;top:3496px;font-size:14px;color:#333}
.s-sub b{color:var(--green);font-size:26px}
.email{left:149px;top:3543px;width:515px;height:47px;background:var(--white);border-radius:24px;padding-left:24px;display:flex;align-items:center;font-size:14px;color:#999}

/* footer */
.f-head{top:3750px;font-size:15px;font-weight:500}
.f-head::after{content:"";display:block;width:56px;height:2px;background:var(--green);margin-top:8px}
.f-list{font-size:14px;line-height:24px;color:var(--muted);list-style:none}
.social{width:30px;height:30px;background:var(--green)}
</style>
</head>
<body>

<!-- header -->
<div class="abs header"></div>
<div class="abs topbar">
  <span><svg width="14" height="14" viewBox="0 0 24 24"><path fill="#fff" d="M6.6 10.8a15 15 0 0 0 6.6 6.6l2.2-2.2c.3-.3.7-.4 1-.2 1.1.4 2.3.6 3.6.6.6 0 1 .4 1 1V20c0 .6-.4 1-1 1A17 17 0 0 1 3 4c0-.6.4-1 1-1h3.5c.6 0 1 .4 1 1 0 1.3.2 2.5.6 3.6.1.3 0 .7-.2 1z"/></svg><b>+1-303-555-0178</b></span>
  <span><svg width="14" height="14" viewBox="0 0 24 24"><circle cx="12" cy="12" r="10" fill="#fff"/><circle cx="12" cy="10" r="3.5" fill="#3fa535"/></svg>My Account ▾</span>
  <span><svg width="16" height="14" viewBox="0 0 24 20"><path fill="#fff" d="M0 1h4l3 11h13l3-8H7"/><circle cx="9" cy="17" r="2" fill="#fff"/><circle cx="19" cy="17" r="2" fill="#fff"/></svg>My Cart ▾</span>
</div>
<div class="abs logo" style="left:149px;top:46px"><i></i>Velvet Beaming</div>
<nav class="nav">
  <a class="active" style="left:398px">Home</a>
  <a style="left:482px">About Us</a>
  <a style="left:582px">Policy</a>
  <a style="left:664px">Returns</a>
  <a style="left:759px">Subscription etc</a>
  <a style="left:908px">Contact Us</a>
</nav>
<svg class="abs" style="left:1030px;top:64px" width="22" height="22" viewBox="0 0 24 24"><circle cx="10" cy="10" r="7" fill="none" stroke="#222" stroke-width="2.5"/><path d="M15 15l6 6" stroke="#222" stroke-width="2.5"/></svg>

<!-- hero -->
<div class="abs hero-bg"></div>
<div class="ph" role="img" aria-label="Smiling woman biting a watermelon slice" style="left:731px;top:108px;width:469px;height:474px;background:radial-gradient(ellipse at 55% 40%,#f1d2c0 0%,#c89a7e 45%,rgba(79,220,202,0) 72%)"></div>
<svg class="abs" style="left:0;top:108px" width="1200" height="570"><polygon points="0,570 1200,393 1200,570" fill="#fff"/></svg>
<div class="ph" role="img" aria-label="Three whitening gel tubes with green leaves and watermelon" style="left:501px;top:284px;width:330px;height:326px;background:linear-gradient(180deg,#f4f7f4 0%,#e4efe2 55%,#52b64a 100%);border-radius:12px"></div>
<div class="ph" role="img" aria-label="Green leaf" style="left:0;top:560px;width:110px;height:118px;background:radial-gradient(ellipse at 20% 70%,#5fb83f,rgba(95,184,63,0) 70%)"></div>
<div class="abs hero-rule"></div>
<div class="abs script hero-1">What your</div>
<div class="abs script hero-2">routine</div>
<div class="abs hero-3">NEEDS</div>
<div class="btn" style="left:217px;top:425px;width:150px;height:50px">SHOP NOW</div>

<!-- history -->
<div class="abs watermark">WHITENING</div>
<div class="ph" role="img" aria-label="Smiling woman in a white tee pointing to the right" style="left:149px;top:718px;width:406px;height:447px;background:linear-gradient(180deg,#d8ad8e 0%,#efefef 35%,#e7e7e7 75%,#4f6d8f 100%);border-radius:10px"></div>
<div class="ph" role="img" aria-label="Whitening gel tube in a green circle" style="left:577px;top:807px;width:100px;height:100px;border-radius:50%;background:radial-gradient(circle,#f4f4f4 0 30%,var(--green) 31%)"></div>
<div class="abs serif h-title" style="font-weight:700">Our History</div>
<div class="abs h-sub">create a <b>whitening</b> <em>gel</em></div>
<p class="abs h-text">There are many variations of passages of Lorem Ipsum available, but the majority have suffered alteration in some form, by injected</p>
<div class="btn" style="left:601px;top:1103px;width:190px;height:48px">READ MORE</div>

<!-- intro band -->
<div class="abs band"></div>
<div class="ph" role="img" aria-label="Woman with flowing hair beside three whitening gel tubes" style="left:569px;top:1238px;width:631px;height:401px;background:radial-gradient(ellipse at 30% 45%,#c9a58a 0%,#8c6b57 35%,rgba(85,85,85,0) 62%),radial-gradient(ellipse at 80% 60%,#f2f2f2 0%,#6fbf55 30%,rgba(85,85,85,0) 55%)"></div>
<div class="abs band-kicker">PRODUCT INTRODUCTION</div>
<div class="abs band-1">IT IS A LONG</div>
<div class="abs band-2">ESTABLISHED</div>
<div class="abs band-text">There are many variations of passages of Lorem Ipsum available</div>
<div class="btn" style="left:149px;top:1520px;width:164px;height:48px">SHOP NOW
  <svg width="18" height="12" viewBox="0 0 18 12"><path d="M0 6h16M11 1l5 5-5 5" stroke="#fff" stroke-width="2" fill="none"/></svg></div>

<!-- product -->
<div class="abs frame"></div>
<div class="abs thumb" style="left:221px;top:1809px"></div>
<div class="abs thumb" style="left:221px;top:1887px"></div>
<div class="abs thumb" style="left:221px;top:1966px"></div>
<div class="abs thumb" style="left:221px;top:2044px"></div>
<div class="ph" role="img" aria-label="Whitening gel tube standing upright" style="left:335px;top:1747px;width:130px;height:407px;background:linear-gradient(180deg,#f6f6f6 0%,#f6f6f6 40%,#4bb043 60%,#3fa535 90%,#cfcfcf 100%);border-radius:8px 8px 4px 4px"></div>
<div class="abs p-title">Product Introduction</div>
<div class="abs p-sub">With Whitening gel 16000M</div>
<div class="abs stars"><svg width="80" height="12" viewBox="0 0 80 12"><g fill="#f0c419"><path id="st" d="M6 0l1.8 3.8 4.2.5-3.1 2.9.8 4.1L6 9.3 2.3 11.3l.8-4.1L0 4.3l4.2-.5z"/><use href="#st" x="17"/><use href="#st" x="34"/><use href="#st" x="51"/><use href="#st" x="68"/></g></svg></div>
<div class="abs reviews">(10) Reviews &nbsp;&nbsp;&nbsp;|&nbsp;&nbsp;&nbsp; Write an Review</div>
<p class="abs p-text">A gentle whitening gel that lifts everyday stains from coffee and tea, leaving teeth brighter and breath fresh after each short session.</p>
<div class="abs" style="left:588px;top:1950px;width:24px;height:1px"></div>
<div class="abs" style="left:588px;top:1950px;display:grid;grid-template-columns:218px 200px;row-gap:12px">
  <div class="check"><svg width="18" height="18"><circle cx="9" cy="9" r="8" fill="none" stroke="#3fa535" stroke-width="1.5"/><path d="M5 9l3 3 5-6" stroke="#3fa535" stroke-width="2" fill="none"/></svg>Safe on tooth enamel</div>
  <div class="check"><svg width="18" height="18"><circle cx="9" cy="9" r="8" fill="none" stroke="#3fa535" stroke-width="1.5"/><path d="M5 9l3 3 5-6" stroke="#3fa535" stroke-width="2" fill="none"/></svg>Fresh mint flavour gel</div>
  <div class="check"><svg width="18" height="18"><circle cx="9" cy="9" r="8" fill="none" stroke="#3fa535" stroke-width="1.5"/><path d="M5 9l3 3 5-6" stroke="#3fa535" stroke-width="2" fill="none"/></svg>Results within two weeks</div>
  <div class="check"><svg width="18" height="18"><circle cx="9" cy="9" r="8" fill="none" stroke="#3fa535" stroke-width="1.5"/><path d="M5 9l3 3 5-6" stroke="#3fa535" stroke-width="2" fill="none"/></svg>Kind to sensitive gums</div>
  <div class="check"><svg width="18" height="18"><circle cx="9" cy="9" r="8" fill="none" stroke="#3fa535" stroke-width="1.5"/><path d="M5 9l3 3 5-6" stroke="#3fa535" stroke-width="2" fill="none"/></svg>No harsh peroxide burn</div>
  <div class="check"><svg width="18" height="18"><circle cx="9" cy="9" r="8" fill="none" stroke="#3fa535" stroke-width="1.5"/><path d="M5 9l3 3 5-6" stroke="#3fa535" stroke-width="2" fill="none"/></svg>Easy daily brush routine</div>
</div>
<div class="abs" style="left:588px;top:2056px;width:385px;height:1px;background:var(--line)"></div>
<div class="abs price">$40.00</div>
<div class="abs qty"><span>-</span><span>1</span><span>+</span></div>
<div class="btn" style="left:767px;top:2124px;width:164px;height:50px">ADD TO CART</div>

<!-- tabs -->
<div class="abs tabs-bg"></div>
<div class="abs tab-line"></div>
<div class="abs tab active" style="left:217px">Product Info</div>
<div class="abs tab" style="left:474px">Suggested Use</div>
<div class="abs tab" style="left:737px">Whitening gel</div>
<div class="abs tab" style="left:997px">Ingredients</div>
<div class="abs" style="left:347px;top:2290px;width:1px;height:22px;background:#7fd9c3"></div>
<div class="abs" style="left:604px;top:2290px;width:1px;height:22px;background:#7fd9c3"></div>
<div class="abs" style="left:868px;top:2290px;width:1px;height:22px;background:#7fd9c3"></div>

<div class="abs t-head" style="top:2356px">It is a long established fact that a reader ?</div>
<p class="abs t-text" style="top:2396px;width:902px">Our whitening gel was shaped by years of listening to customers who wanted a brighter smile without sore teeth. Each tube holds a smooth formula that clings to the enamel, works for a few quiet minutes and rinses away clean. It suits a busy morning, a slow evening or a quick touch before a night out, and it travels well in any bag. Most users notice a lighter shade within the first week.</p>
<div class="abs t-head" style="top:2465px">It is a long established fact that a reader ?</div>
<p class="abs t-text" style="top:2505px;width:902px">Brush gently for two minutes after your usual toothpaste, then spread a thin layer of gel across the front teeth. Leave it in place for ten minutes, avoid food and drink, then rinse with cool water. Repeat once a day for fourteen days, and after that use it twice a week to keep the glow.</p>
<div class="abs t-head" style="top:2592px">It is a long established fact that a reader ?</div>
<p class="abs t-text" style="top:2632px;width:520px">Every batch is mixed in small runs and checked for texture, taste and strength before it ships. The gel stays calm on gums, leaves no chalky film and keeps its colour for months after opening.</p>
<p class="abs t-text" style="top:2732px;width:520px">Store the tube with the cap closed, away from direct sun. Ask your dentist first if you wear braces, are pregnant or have recent fillings on your front teeth.</p>
<div class="ph" role="img" aria-label="Video still of a woman smiling and holding a gel tube" style="left:704px;top:2595px;width:347px;height:203px;border:3px solid var(--dark);background:linear-gradient(90deg,#f2f2f2 0%,#dedede 40%,#c7a18a 75%,#eeeeee 100%)"></div>
<svg class="abs" style="left:846px;top:2667px" width="60" height="60" viewBox="0 0 60 60"><circle cx="30" cy="30" r="29" fill="#3fa535" stroke="#c9efc0" stroke-width="2"/><path d="M24 19l17 11-17 11z" fill="#fff"/></svg>

<!-- news -->
<div class="abs news-1">News</div>
<div class="abs" style="left:522px;top:2948px;width:70px;height:2px;background:var(--ink)"></div>
<div class="abs news-2">from Blog</div>

<div class="ph" role="img" aria-label="Blog photo of a smiling woman with curly hair" style="left:149px;top:2999px;width:209px;height:176px;background:linear-gradient(135deg,#6a4a35,#d9a98a 50%,#e4b547)"></div>
<div class="abs date" style="left:336px;top:3021px"><b>18</b><small>June</small></div>
<div class="abs topic" style="left:149px;top:3196px">TOPIC NAME</div>
<div class="abs n-title" style="left:149px;top:3218px">It is a long established fact that a reader will be distracted by the</div>
<div class="abs more" style="left:290px;top:3300px">Read More »</div>

<div class="ph" role="img" aria-label="Blog photo of a smiling woman with dark hair" style="left:479px;top:2999px;width:209px;height:176px;background:linear-gradient(135deg,#4a3126,#e1b59a 55%,#f3e9e1)"></div>
<div class="abs date" style="left:666px;top:3021px"><b>14</b><small>June</small></div>
<div class="abs topic" style="left:479px;top:3196px">TOPIC NAME</div>
<div class="abs n-title" style="left:479px;top:3218px">distracted by the readable content</div>
<div class="abs more" style="left:620px;top:3300px">Read More »</div>

<div class="ph" role="img" aria-label="Blog close-up photo of a bright smile with red lips" style="left:793px;top:2999px;width:209px;height:176px;background:linear-gradient(135deg,#f2ded3,#e7b7a4 45%,#c23b3b 70%,#f5e6dc)"></div>
<div class="abs date" style="left:980px;top:3021px"><b>8</b><small>June</small></div>
<div class="abs topic" style="left:793px;top:3196px">TOPIC NAME</div>
<div class="abs n-title" style="left:793px;top:3218px">that a reader will be distracted by the readable content</div>
<div class="abs more" style="left:928px;top:3300px">Read More »</div>

<!-- signup -->
<div class="abs sign-bg"></div>
<div class="ph" role="img" aria-label="Laughing woman with a bright white smile" style="left:677px;top:3386px;width:523px;height:266px;background:linear-gradient(90deg,rgba(236,227,227,0) 0%,#e9c7b3 40%,#d6a88d 70%,#f1e5df 100%)"></div>
<div class="abs s-title">Sign Up &amp; Save</div>
<div class="abs s-sub">Sing Up for Updates &amp; Special <b>Offer</b></div>
<div class="abs email">Email address</div>
<div class="btn" style="left:672px;top:3541px;width:134px;height:50px">SUBSCRIBE</div>

<!-- footer -->
<div class="abs logo" style="left:149px;top:3746px"><i></i>Velvet Beaming</div>
<div class="abs" style="left:149px;top:3802px;font-size:19px;font-weight:700;color:var(--green)">Whitening gel</div>
<p class="abs" style="left:149px;top:3852px;width:270px;font-size:13px;line-height:20px;color:var(--muted)">It is a long established fact that a reader will be distracted by the readable content of a page when looking at its layout.</p>

<div class="abs f-head" style="left:498px">Quick Links</div>
<ul class="abs f-list" style="left:498px;top:3792px">
  <li>Home</li><li>About Us</li><li>Policy</li><li>Returns</li><li>Subscription etc</li><li>Contact Us</li>
</ul>
<div class="abs f-head" style="left:707px">Product</div>
<ul class="abs f-list" style="left:707px;top:3792px;width:120px">
  <li>whitening gel</li><li>There are many variations of passages of Lorem Ipsum available, but the majority humour</li>
</ul>
<div class="abs f-head" style="left:916px">Contact with Us</div>
<div class="abs social" style="left:916px;top:3800px"></div>
<div class="abs social" style="left:958px;top:3800px"></div>
<div class="abs social" style="left:916px;top:3846px"></div>
<div class="abs social" style="left:958px;top:3846px"></div>

<div class="abs" style="left:149px;top:4004px;width:902px;height:1px;background:var(--line)"></div>
<div class="abs" style="left:0;top:4024px;width:1200px;text-align:center;font-size:12px;color:var(--muted)">© 2018 Whitening gel, LLC</div>

</body>
</html>
```